Software company specialized in data analytics and professional services

We need a landing page design for our business. It should include our logo design. It should have multiple sections :
- stylish head
- what we do (data analytics software, professional services)
- contact form

Target Market(s)

Companies, B2B

Industry/Entity Type

Data

Number of Pages Required

1 page

Font styles to use
Sans Serif

Requirements
Must have
• Dark theme
Should not have
• Gradients on buttons

```html
<!DOCTYPE html>
<html lang="en">
<head>
<meta charset="utf-8">
<title>Northquill — Data Analytics &amp; Professional Services</title>
<link rel="stylesheet" href="https://fonts.googleapis.com/css2?family=Rubik:wght@500;700;800;900&family=Inter:wght@400;500;600;700&display=swap">
<style>
:root{
  --bg:#0e0b35;
  --bg-deep:#09072a;
  --field:#1c1a47;
  --magenta:#e0139c;
  --teal:#12799a;
  --white:#ffffff;
  --muted:#d9d7ee;
  --line:#2a2760;
  --badge:#1b5f8a;
}
*{box-sizing:border-box;margin:0;padding:0}
html,body{width:1200px;height:3841px;overflow:hidden}
body{background:var(--bg);color:var(--white);font-family:"Inter",sans-serif;position:relative}
.abs{position:absolute;z-index:1}
.brand{font-family:"Rubik",sans-serif;font-weight:500;font-size:30px;letter-spacing:2px;color:var(--white)}
.nav-links{left:335px;top:46px;display:flex;gap:30px;font-size:11px;letter-spacing:.3px;color:var(--muted);z-index:2}
.btn{display:flex;align-items:center;justify-content:center;gap:8px;font-family:"Inter",sans-serif;font-weight:700;font-size:13px;letter-spacing:.3px;color:var(--white);text-transform:uppercase;text-decoration:none}
.btn-solid{background:var(--magenta);border-radius:3px}
.btn-outline{border:2px solid var(--magenta);border-radius:3px}
.arrow{width:16px;height:10px}
.hero-visual{z-index:0;left:590px;top:0;width:610px;height:660px;background:radial-gradient(ellipse at 62% 42%,#2b3c9e 0%,#1a2374 30%,#141457 55%,rgba(14,11,53,0) 75%)}
.hero-title{left:63px;top:172px;font-family:"Rubik",sans-serif;font-weight:800;font-size:58px;line-height:60px;letter-spacing:-.5px}
.t-teal{color:var(--teal)}
.t-magenta{color:var(--magenta)}
.hero-text{left:63px;top:376px;width:540px;font-size:15px;line-height:22px;color:var(--muted)}
.section-title{font-family:"Rubik",sans-serif;font-weight:800;font-size:64px;line-height:58px}
.services-text{left:63px;top:1027px;width:300px;font-size:13.5px;line-height:19px;color:var(--muted)}
.card{width:297px;height:342px;border:2px solid var(--magenta);border-radius:4px;padding:22px 22px}
.card-icon{width:62px;height:62px;display:block}
.card h3{font-family:"Rubik",sans-serif;font-weight:700;font-size:22px;color:var(--teal);margin-top:14px}
.card p{font-size:13px;line-height:17.5px;color:var(--muted);margin-top:6px;height:140px;overflow:hidden}
.card .more{display:flex;align-items:center;gap:6px;margin-top:14px;font-size:12.5px;font-weight:700;color:var(--magenta)}
.partner{left:63px;top:2137px;width:1074px;height:385px;border-radius:30px;background:linear-gradient(100deg,#0f6c8f 0%,#123e7a 45%,#1c1a5e 80%,#1d1655 100%)}
.partner-badge{left:128px;top:68px;width:249px;height:249px;border-radius:50%;background:var(--badge);opacity:.8}
.partner h2{left:563px;top:70px;font-family:"Rubik",sans-serif;font-weight:800;font-size:58px;line-height:58px}
.partner p{left:563px;top:196px;width:380px;font-size:13.5px;line-height:19px;color:var(--muted)}
.contact-title{left:0;width:1200px;top:2608px;text-align:center;font-family:"Rubik",sans-serif;font-weight:800;font-size:58px}
.contact-sub{left:0;width:1200px;top:2683px;text-align:center;font-size:13.5px;line-height:19px;color:var(--muted)}
.field{width:345px;height:54px;background:var(--field);border-radius:3px;padding:0 20px;display:flex;align-items:center;font-size:14px;color:#a9a7c8}
.field.active{border:2px solid var(--magenta)}
.field.message{width:718px;height:109px;align-items:flex-start;padding-top:18px}
.consent{left:241px;top:3160px;width:720px;display:flex;gap:14px;font-size:14px;line-height:19px;color:var(--muted)}
.check{flex:none;width:22px;height:22px;border:2px solid var(--magenta);border-radius:3px;margin-top:4px}
.decor{z-index:0;opacity:.85}
.divider{left:63px;top:3367px;width:1074px;height:1px;background:var(--line)}
.foot-col h4{font-family:"Rubik",sans-serif;font-weight:700;font-size:19px;letter-spacing:.3px;padding-bottom:8px;position:relative}
.foot-col h4::after{content:"";position:absolute;left:0;bottom:0;width:48px;height:3px;background:var(--magenta)}
.foot-col ul{list-style:none;margin-top:22px}
.foot-col li{font-size:15.5px;color:var(--muted);height:35px}
.contact-list li{display:flex;align-items:center;gap:12px}
.bottom-bar{left:0;top:3786px;width:1200px;height:55px;background:var(--bg-deep);font-size:13.5px;color:var(--muted)}
</style>
</head>
<body>

<!-- Hero backdrop -->
<div class="abs hero-visual" role="img" aria-label="Glowing digital human profile made of data particles"></div>

<!-- Header -->
<div class="abs brand" style="left:63px;top:36px">NORTHQUILL</div>
<nav class="abs nav-links">
  <span>ABOUT US</span><span>SERVICES</span><span>INDUSTRIES</span><span>CASE STUDIES</span><span>INSIGHTS</span><span>CONTACT US</span>
</nav>
<a class="abs btn btn-solid" style="left:952px;top:31px;width:163px;height:45px;font-size:11.5px;z-index:2">Get in touch
  <svg class="arrow" viewBox="0 0 16 10"><path d="M0 5h14M10 1l4 4-4 4" fill="none" stroke="#fff" stroke-width="1.6"/></svg></a>

<!-- Hero -->
<h1 class="abs hero-title">Transform<br><span class="t-teal">Raw Data</span> into<br><span class="t-magenta">Business Insights</span></h1>
<p class="abs hero-text">Unlock the power of your data with Northquill, a leading software company specializing in data analytics and other professional services. At Northquill, we believe in transforming raw data into actionable insights, empowering businesses to make informed decisions and drive success.</p>
<a class="abs btn btn-outline" style="left:63px;top:501px;width:192px;height:52px">Our services
  <svg class="arrow" viewBox="0 0 16 10"><path d="M0 5h14M10 1l4 4-4 4" fill="none" stroke="#fff" stroke-width="1.6"/></svg></a>
<a class="abs btn btn-outline" style="left:285px;top:501px;width:193px;height:52px">Contact us
  <svg class="arrow" viewBox="0 0 16 10"><path d="M0 5h14M10 1l4 4-4 4" fill="none" stroke="#fff" stroke-width="1.6"/></svg></a>

<!-- Services -->
<h2 class="abs section-title" style="left:63px;top:902px">Our<br><span class="t-teal">Services</span></h2>
<p class="abs services-text">Explore a world of possibilities with Northquill – your trusted partner in navigating the data landscape and unlocking the true potential of your business.</p>
<a class="abs btn btn-solid" style="left:63px;top:1125px;width:192px;height:53px">Contact us
  <svg class="arrow" viewBox="0 0 16 10"><path d="M0 5h14M10 1l4 4-4 4" fill="none" stroke="#fff" stroke-width="1.6"/></svg></a>

<div class="abs card" style="left:841px;top:738px">
  <svg class="card-icon" viewBox="0 0 62 62" fill="none" stroke="#e0139c" stroke-width="2"><path d="M6 56h50M10 56V40h6v16M22 56V32h6v24M34 56V36h6v20M46 56V20h6v36M10 32l12-10 12 6 14-16"/><circle cx="48" cy="12" r="3"/></svg>
  <h3>Data Governance</h3>
  <p>Northquill's Data Governance services establish and uphold the principles of data integrity, quality, and compliance. We guide you through the creation and implementation of effective governance policies, ensuring that your data not only speaks volumes but does so with ac...</p>
  <span class="more">LEARN MORE <svg class="arrow" viewBox="0 0 16 10"><path d="M0 5h14M10 1l4 4-4 4" fill="none" stroke="#e0139c" stroke-width="1.6"/></svg></span>
</div>
<div class="abs card" style="left:483px;top:891px">
  <svg class="card-icon" viewBox="0 0 62 62" fill="none" stroke="#e0139c" stroke-width="2"><circle cx="36" cy="24" r="18"/><path d="M23 37L6 54l3 3 17-17M28 32V22M34 32V16M40 32V20M46 32V26"/></svg>
  <h3>Data Analytics</h3>
  <p>At Northquill, we excel in the art of deciphering data. Our Data Analytics services go beyond mere numbers, transforming raw information into actionable insights. Whether it's predictive modeling, trend analysis, or customized reporting, our expert team ensures that your data becom...</p>
  <span class="more">LEARN MORE <svg class="arrow" viewBox="0 0 16 10"><path d="M0 5h14M10 1l4 4-4 4" fill="none" stroke="#e0139c" stroke-width="1.6"/></svg></span>
</div>
<div class="abs card" style="left:841px;top:1143px">
  <svg class="card-icon" viewBox="0 0 62 62" fill="none" stroke="#e0139c" stroke-width="2"><path d="M16 40h-2a10 10 0 010-20 16 16 0 0131-4 11 11 0 013 22h-4"/><rect x="20" y="22" width="20" height="7" rx="2"/><rect x="20" y="31" width="20" height="7" rx="2"/><rect x="20" y="40" width="20" height="7" rx="2"/><path d="M30 47v8M22 55h16"/></svg>
  <h3>Cloud Computing</h3>
  <p>Elevate your operations with Northquill's Cloud Computing services. Our experts seamlessly transition your infrastructure to the cloud, providing scalability, flexibility, and cost-efficiency. Whether it's migrating existing systems or developing cloud-native applications...</p>
  <span class="more">LEARN MORE <svg class="arrow" viewBox="0 0 16 10"><path d="M0 5h14M10 1l4 4-4 4" fill="none" stroke="#e0139c" stroke-width="1.6"/></svg></span>
</div>
<div class="abs card" style="left:483px;top:1297px">
  <svg class="card-icon" viewBox="0 0 62 62" fill="none" stroke="#e0139c" stroke-width="2"><circle cx="31" cy="31" r="15"/><rect x="25" y="30" width="12" height="10" rx="1"/><path d="M27 30v-4a4 4 0 018 0v4M31 4v12M31 46v12M4 31h12M46 31h12M12 12l8 8M42 42l8 8M50 12l-8 8M20 42l-8 8"/></svg>
  <h3>Cyber Security</h3>
  <p>Security is at the core of everything we do. Northquill's Cyber Security services are designed to safeguard your valuable data assets. From threat assessments to robust encryption protocols, we deploy cutting-edge measures to protect against cyber threats. Trust us to fortify your digita...</p>
  <span class="more">LEARN MORE <svg class="arrow" viewBox="0 0 16 10"><path d="M0 5h14M10 1l4 4-4 4" fill="none" stroke="#e0139c" stroke-width="1.6"/></svg></span>
</div>
<div class="abs card" style="left:841px;top:1547px">
  <svg class="card-icon" viewBox="0 0 62 62" fill="none" stroke="#e0139c" stroke-width="2"><ellipse cx="22" cy="10" rx="16" ry="5"/><path d="M6 10v30c0 3 7 5 16 5M38 10v14M6 20c0 3 7 5 16 5s16-2 16-5M6 30c0 3 7 5 16 5"/><circle cx="44" cy="42" r="7"/><path d="M44 29v5M44 50v5M31 42h5M52 42h5M35 33l3 3M50 48l3 3M53 33l-3 3M38 48l-3 3"/></svg>
  <h3>Data Engineering</h3>
  <p>Building a robust data foundation is key to unlocking analytics potential. Northquill's Data Engineering services specialize in seamless data integration, migration, and warehousing. Our team architects scalable and efficient solutions, ensuring your data infrastructure is...</p>
  <span class="more">LEARN MORE <svg class="arrow" viewBox="0 0 16 10"><path d="M0 5h14M10 1l4 4-4 4" fill="none" stroke="#e0139c" stroke-width="1.6"/></svg></span>
</div>
<div class="abs card" style="left:483px;top:1701px">
  <svg class="card-icon" viewBox="0 0 62 62" fill="none" stroke="#e0139c" stroke-width="2"><path d="M28 8a10 10 0 00-16 4 9 9 0 00-6 14 9 9 0 004 14 10 10 0 0018 8z"/><path d="M28 8v40"/><rect x="34" y="22" width="14" height="14" rx="2"/><path d="M38 22v-6M44 22v-6M38 36v6M44 36v6M48 26h6M48 32h6M28 29h6"/></svg>
  <h3>AI / ML</h3>
  <p>Embrace the future with Northquill's AI/ML services. We bring the power of artificial intelligence and machine learning to your fingertips, enabling you to glean insights, predict trends, and automate processes. From recommendation systems to anomaly detection, our AI/ML solutions open...</p>
  <span class="more">LEARN MORE <svg class="arrow" viewBox="0 0 16 10"><path d="M0 5h14M10 1l4 4-4 4" fill="none" stroke="#e0139c" stroke-width="1.6"/></svg></span>
</div>

<!-- Partner band -->
<section class="abs partner">
  <div class="abs partner-badge" role="img" aria-label="Cloud partner certification badge"></div>
  <h2 class="abs"><span class="t-teal">Nimbra</span> Partner<br>Services</h2>
  <p class="abs">Transform your company today by joining the Nimbra (Nimbra Cloud Services) Cloud Journey with Northquill.</p>
  <a class="abs btn btn-solid" style="left:561px;top:264px;width:193px;height:53px">Contact us
    <svg class="arrow" viewBox="0 0 16 10"><path d="M0 5h14M10 1l4 4-4 4" fill="none" stroke="#fff" stroke-width="1.6"/></svg></a>
</section>

<!-- Contact -->
<div class="abs decor" style="left:0;top:2653px;width:122px;height:313px;border-radius:0 60px 60px 0;background:linear-gradient(180deg,#12799a 0%,#6a12b8 50%,#1d1a66 100%)" role="img" aria-label="Decorative gradient shape"></div>
<div class="abs decor" style="left:1076px;top:2966px;width:124px;height:314px;border-radius:60px 0 0 60px;background:linear-gradient(180deg,#1d1a66 0%,#e0139c 45%,#12799a 100%)" role="img" aria-label="Decorative gradient shape"></div>

<h2 class="abs contact-title">Contact Us Today!</h2>
<p class="abs contact-sub">Explore the full potential of your data with Northquill. Schedule a consultation<br>with us today and unlock valuable insights for your business.</p>

<div class="abs field active" style="left:241px;top:2766px">First Name*</div>
<div class="abs field" style="left:616px;top:2766px">Last Name*</div>
<div class="abs field" style="left:241px;top:2850px">Email Address*</div>
<div class="abs field" style="left:616px;top:2850px">Phone Number*</div>
<div class="abs field" style="left:241px;top:2933px">Company Name*</div>
<div class="abs field" style="left:616px;top:2933px">Subject*</div>
<div class="abs field message" style="left:241px;top:3017px">Message*</div>
<div class="abs consent"><span class="check"><svg width="18" height="18" viewBox="0 0 18 18"><path d="M4 9l3 3 7-7" fill="none" stroke="#e0139c" stroke-width="2"/></svg></span>
  <span>I agree to allow Northquill to use my personal information to send me electronic messages and marketing communications as described in the Privacy Policy.</span></div>
<a class="abs btn btn-solid" style="left:502px;top:3227px;width:193px;height:54px">Submit
  <svg class="arrow" viewBox="0 0 16 10"><path d="M0 5h14M10 1l4 4-4 4" fill="none" stroke="#fff" stroke-width="1.6"/></svg></a>

<!-- Footer -->
<div class="abs divider"></div>
<div class="abs brand" style="left:63px;top:3451px">NORTHQUILL</div>
<div class="abs foot-col" style="left:383px;top:3450px">
  <h4>MAIN LINKS</h4>
  <ul><li>About Us</li><li>Services</li><li>Industries</li><li>Case Studies</li><li>Insights</li><li>Contact Us</li></ul>
</div>
<div class="abs foot-col" style="left:638px;top:3450px">
  <h4>SERVICES</h4>
  <ul><li>Data Analytics</li><li>Data Governance</li><li>Cyber Security</li><li>Cloud Computing</li><li>AI / ML</li><li>Data Engineering</li></ul>
</div>
<div class="abs foot-col" style="left:924px;top:3450px">
  <h4>CONTACT US</h4>
  <ul class="contact-list">
    <li><svg width="16" height="12" viewBox="0 0 16 12"><rect x="1" y="1" width="14" height="10" fill="none" stroke="#e0139c" stroke-width="1.6"/><path d="M1 1l7 6 7-6" fill="none" stroke="#e0139c" stroke-width="1.6"/></svg>hello@northquill.example</li>
    <li><svg width="16" height="16" viewBox="0 0 16 16"><path d="M3 1l3 1 1 4-2 1a9 9 0 004 4l1-2 4 1 1 3-2 2C7 15 1 9 1 3z" fill="#e0139c"/></svg>+1 555 010 2040</li>
    <li><svg width="14" height="18" viewBox="0 0 14 18"><path d="M7 17S1 10 1 6.5a6 6 0 0112 0C13 10 7 17 7 17z" fill="#e0139c"/><circle cx="7" cy="6.5" r="2.2" fill="#0e0b35"/></svg>Your Office Address Here</li>
  </ul>
</div>

<div class="abs bottom-bar">
  <span class="abs" style="left:65px;top:19px">©2023 Northquill. All rights reserved.</span>
  <span class="abs" style="left:497px;top:19px">Privacy Policy</span>
  <span class="abs" style="left:599px;top:17px;width:1px;height:22px;background:#4a4780"></span>
  <span class="abs" style="left:617px;top:19px">Terms of Use</span>
  <span class="abs" style="left:1092px;top:20px;width:17px;height:17px;border-radius:50%;background:#fff" aria-label="Social profile"></span>
  <span class="abs" style="left:1119px;top:20px;width:17px;height:17px;border-radius:2px;background:#fff" aria-label="Social profile"></span>
</div>

</body>
</html>
```